Business Card Design

We are a state licensed general contractor on the south east coast of Florida. We are a remodeling and home repairs business that have been in business for 14 years. Since we are located on the coast and our business name is Ridgeway Builders of Lower Meadow, Inc, we would like a "Ridgeway" themed design that would appeal to more affluent customers. I would like to see light blue colors with waves incorporated into the design. I would also like the design to communicate a modern, confident, responsible company character.

Industry/Entity Type

Contractor

Contact Information for Business Card

Tim Harlow 555-276-3148

```html
<!DOCTYPE html>
<html lang="en">
<head>
<meta charset="utf-8">
<title>Ridgeway Builders – Business Card</title>
<link rel="stylesheet" href="https://fonts.googleapis.com/css2?family=Lato:wght@400;700&display=swap">
<style>
  :root {
    --page-bg: #e9ebee;
    --card-white: #ffffff;
    --brand-navy: #1d4f9c;
    --brand-teal: #3fa7d6;
    --text-on-blue: #ffffff;
    --text-soft: #e3f2fc;
  }
  html, body {
    margin: 0;
    width: 1200px;
    height: 600px;
    overflow: hidden;
    background: var(--page-bg);
    font-family: "Lato", Arial, sans-serif;
  }
  .card {
    position: absolute;
    left: 162px;
    top: 50px;
    width: 875px;
    height: 500px;
    border-radius: 28px;
    overflow: hidden;
    background: var(--card-white);
    box-shadow: 0 10px 30px rgba(20, 50, 90, 0.18);
  }
  .card-waves {
    position: absolute;
    inset: 0;
    width: 100%;
    height: 100%;
  }
  .brand {
    position: absolute;
    left: 70px;
    top: 205px;
    display: flex;
    align-items: center;
    gap: 14px;
  }
  .brand-dot {
    width: 26px;
    height: 26px;
    border-radius: 50%;
    background: var(--brand-teal);
  }
  .brand-name {
    font-size: 42px;
    font-weight: 700;
    color: var(--brand-navy);
    letter-spacing: 0.5px;
    line-height: 1;
  }
  .brand-name small {
    display: block;
    font-size: 13px;
    letter-spacing: 5px;
    margin-top: 8px;
    text-transform: uppercase;
  }
  .person {
    position: absolute;
    left: 440px;
    bottom: 44px;
    color: var(--text-on-blue);
    line-height: 1.3;
  }
  .person-name {
    font-size: 24px;
    font-weight: 700;
  }
  .person-role {
    font-size: 18px;
    font-weight: 700;
  }
  .person-detail {
    font-size: 17px;
    color: var(--text-soft);
  }
  .contact {
    position: absolute;
    right: 40px;
    top: 40px;
    list-style: none;
    margin: 0;
    padding: 0;
    color: var(--text-on-blue);
    font-size: 17px;
    text-align: right;
  }
  .contact li {
    display: flex;
    justify-content: flex-end;
    align-items: center;
    gap: 12px;
    line-height: 1.45;
  }
  .contact .address-line { margin-bottom: 14px; }
  .contact .email { margin-top: 22px; font-size: 15px; }
  .contact-icon {
    width: 16px;
    height: 16px;
    flex: none;
  }
  .icon-spacer { width: 16px; flex: none; }
</style>
</head>
<body>
  <article class="card">
    <svg class="card-waves" viewBox="0 0 875 500" aria-hidden="true">
      <defs>
        <linearGradient id="lightBand" x1="0" y1="0" x2="1" y2="1">
          <stop offset="0" stop-color="#a8dcf1"/>
          <stop offset="1" stop-color="#4fb0de"/>
        </linearGradient>
        <linearGradient id="deepBand" x1="0" y1="0" x2="1" y2="0.6">
          <stop offset="0" stop-color="#3a9ad6"/>
          <stop offset="0.45" stop-color="#1569b8"/>
          <stop offset="1" stop-color="#0d4f9a"/>
        </linearGradient>
      </defs>
      <path d="M470,0 C360,70 400,260 280,390 C230,445 180,480 140,500 L875,500 L875,0 Z" fill="url(#lightBand)"/>
      <path d="M600,0 C470,55 500,250 380,380 C320,445 270,480 235,500 L875,500 L875,0 Z" fill="url(#deepBand)"/>
      <path d="M600,0 C470,55 500,250 380,380 C320,445 270,480 235,500" fill="none" stroke="#ffffff" stroke-width="3"/>
    </svg>

    <div class="brand">
      <span class="brand-dot"></span>
      <div class="brand-name">Ridgeway<small>Builders</small></div>
    </div>

    <div class="person">
      <div class="person-name">Tim Harlow</div>
      <div class="person-role">Owner</div>
      <div class="person-detail">General Contractors</div>
      <div class="person-detail">CGC041286</div>
    </div>

    <ul class="contact">
      <li>4218 Harrow Lane
        <svg class="contact-icon" viewBox="0 0 16 16"><path d="M8 1a5 5 0 0 0-5 5c0 4 5 9 5 9s5-5 5-9a5 5 0 0 0-5-5zm0 7a2 2 0 1 1 0-4 2 2 0 0 1 0 4z" fill="#fff"/></svg>
      </li>
      <li class="address-line">Fernbrook, FL 33901<span class="icon-spacer"></span></li>
      <li>555.276.3148
        <svg class="contact-icon" viewBox="0 0 16 16"><path d="M4 1l2.5 3-1.5 2c1 2 3 4 5 5l2-1.5 3 2.5-1.5 2C7 15 1 9 2 2.5z" fill="#fff"/></svg>
      </li>
      <li>555.276.4410
        <svg class="contact-icon" viewBox="0 0 16 16"><rect x="4" y="1" width="8" height="14" rx="1.5" fill="none" stroke="#fff" stroke-width="1.6"/><circle cx="8" cy="12.5" r="1" fill="#fff"/></svg>
      </li>
      <li>555.276.5092
        <svg class="contact-icon" viewBox="0 0 16 16"><rect x="2" y="5" width="12" height="7" rx="1" fill="#fff"/><rect x="4" y="1.5" width="8" height="4" fill="none" stroke="#fff" stroke-width="1.4"/><rect x="4.5" y="10" width="7" height="4.5" fill="#fff" stroke="#0f5aa8" stroke-width="1"/></svg>
      </li>
      <li class="email">ridgeway.th@mailbox.com
        <svg class="contact-icon" viewBox="0 0 16 16"><rect x="1.5" y="3.5" width="13" height="9" rx="1" fill="none" stroke="#fff" stroke-width="1.5"/><path d="M2 4l6 5 6-5" fill="none" stroke="#fff" stroke-width="1.5"/></svg>
      </li>
    </ul>
  </article>
</body>
</html>
```